DESIGN FOR FLAVOURED CORDIAL LABEL SUITABLE FOR LOCAL AND EXPORTING COUNTERIES

UPDATED BRIEF ON NUMBER 7
This cordial manufactured in Malaysia, belongs to the same product category as Brivanta and Colvex. Feedback has suggested that the current Tarlo label lacks visual appeal, prompting us to embark on a redesign that enhances visibility and draws consumer attention on store shelves—both locally and internationally.

Key design requirements:
1- The concept should be versatile enough to accommodate various flavors, including Mango, Orange, Grape, Sarsi, Lychee, Rose, and Pineapple, while maintaining a cohesive brand identity.
2- All essential product information must be incorporated, ensuring clarity and compliance with both local and international labeling regulations for export markets.
3- Designers are encouraged to explore creative approaches to make the label visually striking, culturally adaptable, and appealing across diverse consumer demographics.
4- The brand logo may be presented in either white or red, depending on what best suits the overall design while maintaining strong brand recognition in global markets.
5- You may refer to our current label for your perusal.
6- The redesigned label must follow the same artwork dimensions as the existing version. We include the cordial bottle image for your illustration.
7- Real fruit images can be used on label

https://files.vornatek-share.com/d/8kQzPwLmR3tYxVbN2cHsJ7fGdAe9UoKi/view?usp=share_link

Target Market(s)

Malaysia, Archipelago, Middle East, African counteries

Industry/Entity Type

Beverage

Font styles to use
Other font styles liked:
• any fonts suitable but not too fancy.

Requirements
Must have
• Info like in artworks
Nice to have
• creative approaches to visually represent the flavor through design elements such as color palettes, abstract patterns, typography, and symbolic imagery other than pictorial fruits/ graphical fruit

```html
<!DOCTYPE html>
<html lang="en">
<head>
<meta charset="UTF-8">
<title>Tarlo Lychee Flavoured Cordial Label</title>
<link rel="stylesheet" href="https://fonts.googleapis.com/css2?family=Open+Sans:wght@600;700;800&display=swap">
<style>
  :root {
    --backdrop: #e8e8e8;
    --label-white: #f4f1f1;
    --label-blush: #efc9cc;
    --label-red: #d8212f;
    --label-deep: #c81d2a;
    --ink-red: #c8202c;
    --ink-dark-red: #a3151f;
    --fruit-pink: #e56b7c;
    --fruit-flesh: #f6eef0;
    --ink-white: #ffffff;
    --badge-grey: #9a9a9a;
  }
  * { margin: 0; padding: 0; box-sizing: border-box; }
  html, body { width: 1200px; height: 815px; overflow: hidden; }
  body {
    background: var(--backdrop);
    font-family: "Open Sans", Arial, sans-serif;
    display: flex;
    align-items: center;
    justify-content: center;
  }
  .label {
    position: relative;
    width: 700px;
    height: 730px;
    background: linear-gradient(to bottom,
      var(--label-white) 0%,
      var(--label-white) 46%,
      var(--label-blush) 62%,
      var(--label-red) 82%,
      var(--label-deep) 100%);
    text-align: center;
    color: var(--ink-red);
  }
  .brand {
    position: absolute;
    top: 44px; left: 0; right: 0;
  }
  .brand-name {
    font-size: 46px;
    font-weight: 700;
    color: var(--ink-red);
    line-height: 1;
  }
  .brand-since {
    margin-top: 6px;
    font-size: 13px;
    font-weight: 600;
    color: var(--ink-red);
    letter-spacing: 1px;
  }
  .flavour {
    position: absolute;
    top: 150px; left: 0; right: 0;
    font-size: 124px;
    font-weight: 800;
    color: var(--ink-red);
    line-height: 1;
    letter-spacing: -1px;
  }
  .product-type {
    position: absolute;
    top: 286px; left: 0; right: 0;
    display: flex;
    align-items: center;
    justify-content: center;
    gap: 18px;
    font-size: 44px;
    font-weight: 700;
    color: var(--ink-dark-red);
  }
  .product-type::before,
  .product-type::after {
    content: "";
    width: 70px;
    height: 4px;
    background: var(--ink-dark-red);
  }
  .product-type-fr {
    position: absolute;
    top: 354px; left: 0; right: 0;
    font-size: 26px;
    font-weight: 700;
    color: var(--ink-red);
    line-height: 1.25;
  }
  .fruit-visual {
    position: absolute;
    top: 430px; left: 170px;
    width: 360px;
    height: 170px;
    border-radius: 50% 50% 42% 42%;
    background: radial-gradient(ellipse at 50% 55%, var(--fruit-flesh) 0%, var(--fruit-flesh) 18%, var(--fruit-pink) 45%, rgba(229,107,124,0) 72%);
  }
  .halal-badge {
    position: absolute;
    left: 28px; top: 570px;
    width: 58px; height: 58px;
    border-radius: 50%;
    border: 3px solid var(--badge-grey);
    background: var(--label-white);
  }
  .net-content {
    position: absolute;
    bottom: 46px; left: 0; right: 0;
    font-size: 27px;
    font-weight: 700;
    color: var(--ink-white);
  }
</style>
</head>
<body>
  <section class="label">
    <header class="brand">
      <div class="brand-name">Tarlo</div>
      <div class="brand-since">since 1978</div>
    </header>
    <h1 class="flavour">LYCHEE</h1>
    <h2 class="product-type">Flavoured Cordial</h2>
    <p class="product-type-fr">Boisson Concentrée au Goût de Raisin<br>avec Édulcorant</p>
    <div class="fruit-visual" role="img" aria-label="Photograph of fresh lychees, one peeled, with a green leaf"></div>
    <div class="halal-badge" role="img" aria-label="Certification badge"></div>
    <p class="net-content">Net Content / Contenu Net: 840ml</p>
  </section>
</body>
</html>
```